CREATE A KILLER WEBSITE DESIGN

We are a firearms training company that trains CIVILIANS (no police or military pictures - thank you!) to defend themselves and are looking for a killer design that's clean, easy to navigate and modern! We want the newest trends applied to this sight like a scrollable site so you can scroll down and see all the features. We are okay with tweaking the HTML but need the artistic design to look good. I'll provide a link to our current site along with a sight we really like so you can get an idea!

I'm supplying a PowerPoint Design we are going with from another designer so you can match the style to the new site.

PAGES: (Please use information from our current site. We like the information but just want a more polished look similar to the NWDLA site below but in our colors.)
Home - Long Form Scrolling Site. Top fold will be a video with a play button.
Falcon Institute - Seven Level Training Program Info Page That Will Contain A Video.
Contact Us - This will be a page that DOES NOT CONTAIN AN EMAIL ADDRESS. Just a contact us form
Meet The Trainer: Morgan Pellbrook

Our site:
https://www.brisklanewardens.biz

Sights We Like:
https://www.nwdefenseleague.example.com
https://quorvel.example.com
https://brantforgeworks.example.com
https://www.pelnrigear.example.com

Target Market(s)

Men and women ages 21 to 100 years old

Industry/Entity Type

Self Defense

Number of Pages Required

5+ page

Font styles to use
Sans Serif

Colors
f26267

Requirements
Must have
• Clean and engaging. Use of colors that match our logo.
Should not have
• Poor design quality

```html
<!DOCTYPE html>
<html lang="en">
<head>
<meta charset="utf-8">
<title>Brisk Lane Wardens — Concealed Carry Training</title>
<link href="https://fonts.googleapis.com/css2?family=Montserrat:ital,wght@0,400;0,500;0,600;0,700;0,800;1,400&display=swap" rel="stylesheet">
<style>
:root{
  --orange:#f8461b;
  --orange-dark:#d93a12;
  --ink:#2f3333;
  --ink-deep:#232626;
  --hero-a:#3b3f40;
  --hero-b:#1c1e1f;
  --white:#ffffff;
  --muted:#c9cccc;
}
*{margin:0;padding:0;box-sizing:border-box}
html,body{width:1200px;height:2924px;overflow:hidden}
body{font-family:"Montserrat",sans-serif;color:var(--white);background:var(--ink);position:relative}
.abs{position:absolute}

/* hero */
.hero{position:absolute;left:0;top:0;width:1200px;height:468px;background:linear-gradient(110deg,#5a4a3e 0%,var(--hero-a) 35%,var(--hero-b) 100%)}
.nav{position:absolute;top:0;left:0;width:1200px;height:64px;display:flex;align-items:center;justify-content:space-between;padding:0 220px 0 225px;font-size:11px;font-weight:500}
.nav ul{display:flex;gap:26px;list-style:none}
.brand{display:flex;align-items:center;gap:8px;font-weight:700;font-size:12px;letter-spacing:1px;text-transform:uppercase}
.brand i{width:14px;height:14px;background:var(--orange);display:block}
.hero h1{position:absolute;top:120px;width:100%;text-align:center;font-size:27px;font-weight:700;line-height:1.35}
.hero h1 span{color:var(--orange);display:block}
.play{position:absolute;left:568px;top:216px;width:64px;height:64px}
.hero .tag{position:absolute;top:300px;width:100%;text-align:center;font-size:19px;font-weight:600}
.btns{position:absolute;top:354px;width:100%;display:flex;justify-content:center;gap:30px}
.btn{font-size:10px;font-weight:700;text-transform:uppercase;padding:9px 16px;border:1.5px solid var(--white);letter-spacing:.5px}
.btn.fill{background:var(--orange);border-color:var(--orange)}

/* band */
.band{position:absolute;top:468px;left:0;width:1200px;height:72px;background:var(--orange);display:flex;align-items:center;justify-content:center;gap:40px}
.band h2{font-size:19px;font-weight:700;letter-spacing:1px}
.band .btn{padding:6px 18px;font-size:9px}

/* levels */
.levels{position:absolute;top:540px;left:0;width:1200px;height:1060px;background:var(--ink)}
.levels h2{position:absolute;top:38px;width:100%;text-align:center;font-size:22px;font-weight:500;line-height:1.4}
.levels h2 b{color:var(--orange);font-weight:700}
.video{position:absolute;left:388px;top:128px;width:416px;height:204px;border:5px solid var(--white);background:linear-gradient(120deg,#6a6d6d,#2b2d2e)}
.video svg{position:absolute;left:176px;top:70px}
.intro{position:absolute;left:250px;top:360px;width:700px;text-align:center;font-size:11.5px;line-height:1.75;color:var(--muted)}
.intro a{color:var(--orange)}
.tile{position:absolute;width:180px;height:240px;background:linear-gradient(180deg,#7c7f80,#474a4b)}
.tile span{position:absolute;bottom:18px;left:0;width:100%;text-align:center;font-size:9px;font-weight:700;text-transform:uppercase;letter-spacing:.3px}

/* trainer */
.trainer{position:absolute;top:1600px;left:0;width:1200px;height:380px;background:var(--ink)}
.trainer .photo{position:absolute;left:228px;top:0;width:332px;height:292px;background:linear-gradient(160deg,#9a9c9d,#4c4f50)}
.trainer .bio{position:absolute;left:576px;top:16px;width:390px}
.trainer h3{font-size:16px;font-weight:700;margin-bottom:10px}
.trainer p{font-size:10.5px;line-height:1.7;color:var(--orange)}
.press{position:absolute;left:576px;top:312px;display:flex;gap:30px;align-items:center;font-size:12px;font-weight:700}

/* stories */
.stories{position:absolute;top:1980px;left:0;width:1200px;height:540px;background:linear-gradient(180deg,#4a4e4f,#2a2c2d)}
.stories h2{position:absolute;top:50px;width:100%;text-align:center;font-size:24px;font-weight:700;letter-spacing:1px}
.avatar{position:absolute;border-radius:50%;border:3px solid var(--white);background:linear-gradient(160deg,#a8a8a6,#5c5e5e)}
.arrow{position:absolute;top:172px}
.quote{position:absolute;top:316px;left:250px;width:700px;text-align:center;font-size:17px;font-style:italic;line-height:1.6}
.dots{position:absolute;top:440px;width:100%;display:flex;justify-content:center;gap:10px}
.dots i{width:8px;height:8px;border-radius:50%;background:var(--white);opacity:.5}
.dots i.on{opacity:1}

/* footer */
.footer{position:absolute;top:2520px;left:0;width:1200px;height:360px;background:var(--orange)}
.footer ul{position:absolute;left:228px;top:52px;list-style:none;font-size:10px;line-height:2.6}
.contact{position:absolute;left:500px;top:48px;font-size:10px;line-height:2}
.contact h4{font-size:15px;font-weight:700;margin-bottom:4px}
.contact .row{display:flex;align-items:center;gap:8px}
.form{position:absolute;left:770px;top:50px;width:200px;height:232px;background:var(--white);padding:14px}
.form i{display:block;height:18px;border:1px solid #d6d6d6;margin-bottom:9px}
.form i.big{height:68px}
.form b{display:block;width:90px;height:20px;margin:6px auto 0;background:var(--orange);color:var(--white);font-size:8px;text-align:center;line-height:20px;font-weight:700}
.bottom{position:absolute;top:2880px;left:0;width:1200px;height:44px;background:var(--orange-dark);display:flex;align-items:center;justify-content:space-between;padding:0 228px;font-size:9px}
.social{display:flex;gap:8px}
.social i{width:16px;height:16px;border:1px solid var(--white);border-radius:50%;display:block}
</style>
</head>
<body>

<section class="hero" role="img" aria-label="Instructor coaching a civilian student at a shooting range">
  <nav class="nav">
    <ul><li>Home</li><li>Falcon Institute</li><li>Testimonials</li><li>About</li></ul>
    <div class="brand"><i></i>Brisk Lane Wardens</div>
    <ul><li>Upcoming Classes</li><li>Blog</li><li>Videos</li><li>Get Certificate</li></ul>
  </nav>
  <h1>Your life may depend on what <u>you</u> learn in your<span>CONCEALED CARRY CLASS</span></h1>
  <svg class="play" viewBox="0 0 64 64"><circle cx="32" cy="32" r="30" fill="none" stroke="#fff" stroke-width="3"/><path d="M26 20 L46 32 L26 44 Z" fill="#fff"/></svg>
  <p class="tag">Don’t Settle for a Gun Shop class</p>
  <div class="btns"><span class="btn">Upcoming Classes</span><span class="btn fill">Get Certified Now</span></div>
</section>

<section class="band">
  <h2>BRISK LANE WARDENS</h2>
  <span class="btn">Log In</span><span class="btn">Register</span>
</section>

<section class="levels">
  <h2>Our <b>7 LEVELS</b> of training take you from<br>Zero to <b>HERO</b></h2>
  <div class="video" role="img" aria-label="Training video still of a student aiming at the range">
    <svg width="64" height="64" viewBox="0 0 64 64"><circle cx="32" cy="32" r="30" fill="rgba(0,0,0,.35)" stroke="#fff" stroke-width="3"/><path d="M26 20 L46 32 L26 44 Z" fill="#fff"/></svg>
  </div>
  <p class="intro">Wanna hear something funny? Guess what the average person who takes a concealed weapons class knows about real defense? How much is it and how long is it? Can you believe it? We are talking about preparing you for life and death situations and the main concern is "how fast" and "how cheap". WOW — <a>Read More</a></p>
  <div class="tile" style="left:210px;top:492px" role="img" aria-label="Concealed carry class photo"><span>Concealed Carry Class</span></div>
  <div class="tile" style="left:407px;top:492px" role="img" aria-label="Dynamic defense shooting photo"><span>Dynamic Defense Shooting</span></div>
  <div class="tile" style="left:604px;top:492px" role="img" aria-label="Emergency handgun training photo"><span>Emergency Handgun Training</span></div>
  <div class="tile" style="left:801px;top:492px" role="img" aria-label="Virtual threat lab photo"><span>Virtual Threat Lab</span></div>
  <div class="tile" style="left:308px;top:768px" role="img" aria-label="Tactical reality drills photo"><span>Tactical Reality Drills</span></div>
  <div class="tile" style="left:505px;top:768px" role="img" aria-label="Close quarter defense photo"><span>Close Quarter Defense</span></div>
  <div class="tile" style="left:702px;top:768px" role="img" aria-label="Live scenario threat lab photo"><span>Live Scenario Threat Lab</span></div>
</section>

<section class="trainer">
  <div class="photo" role="img" aria-label="Portrait of trainer Morgan Pellbrook"></div>
  <div class="bio">
    <h3>MORGAN PELLBROOK</h3>
    <p>Morgan Pellbrook is a 3rd generation law enforcement trainer and has worked as a part of the civilian defense community for over twenty years. He has taught thousands of students to carry with confidence and calm.<br>He has been featured in national publications and has trained civilians in practical firearms skills and real threat awareness.<br>He is a certified range safety officer and defensive pistol instructor. On other days you will find him at the range helping new shooters find their footing — <b>Read More</b></p>
  </div>
  <div class="press"><span>Channel North</span><span>Meridian TV</span><span>Crestline News</span><span>Harbor One</span></div>
</section>

<section class="stories" role="img" aria-label="Range scene with targets in the background">
  <h2>SUCCESS STORIES</h2>
  <svg class="arrow" style="left:228px" width="24" height="40" viewBox="0 0 24 40"><path d="M20 2 L4 20 L20 38" fill="none" stroke="#fff" stroke-width="3"/></svg>
  <svg class="arrow" style="left:948px" width="24" height="40" viewBox="0 0 24 40"><path d="M4 2 L20 20 L4 38" fill="none" stroke="#fff" stroke-width="3"/></svg>
  <div class="avatar" style="left:364px;top:130px;width:100px;height:100px" role="img" aria-label="Student portrait"></div>
  <div class="avatar" style="left:532px;top:112px;width:136px;height:136px" role="img" aria-label="Student portrait"></div>
  <div class="avatar" style="left:728px;top:130px;width:100px;height:100px" role="img" aria-label="Student portrait"></div>
  <p class="quote">I had never held a gun when I took the Brisk Lane Wardens class and I’m hooked! I’m going all the way to level 7! Thank you Brisk Lane Wardens! - <b>Dana R.</b></p>
  <div class="dots"><i></i><i class="on"></i><i></i></div>
</section>

<footer class="footer">
  <ul><li>Home</li><li>Falcon Institute</li><li>Testimonials</li><li>About</li><li>Upcoming Classes</li><li>Blog</li><li>Videos</li><li>Get Certified</li></ul>
  <div class="contact">
    <h4>Morgan Pellbrook</h4>
    <div>NWDLA Certified Instructor</div>
    <div>Lead Instructor of Brisk Lane Wardens</div>
    <div>Range Safety and Defense Expert</div>
    <div class="row"><svg width="10" height="12" viewBox="0 0 10 12"><path d="M5 0 C2 0 0 2 0 5 C0 8 5 12 5 12 C5 12 10 8 10 5 C10 2 8 0 5 0Z" fill="#fff"/></svg>P.O. Box 4410</div>
    <div>Fairview, ST 00000</div>
    <div class="row"><svg width="10" height="10" viewBox="0 0 10 10"><path d="M2 0 L4 3 L3 4 C4 6 5 7 6 7 L7 6 L10 8 L8 10 C4 10 0 6 0 2Z" fill="#fff"/></svg>(555) 014-2278 · (555) 014-3391</div>
    <div class="row"><svg width="12" height="9" viewBox="0 0 12 9"><rect x=".5" y=".5" width="11" height="8" fill="none" stroke="#fff"/><path d="M.5 .5 L6 5 L11.5 .5" fill="none" stroke="#fff"/></svg>hello@brisklanewardens.biz</div>
  </div>
  <div class="form"><i></i><i></i><i></i><i class="big"></i><b>SEND MESSAGE</b></div>
</footer>
<div class="bottom"><span>© 2024 All rights reserved</span><div class="social"><i></i><i></i><i></i><i></i></div></div>

</body>
</html>
```